Business card design for global fintech startup

Veltrix is a modern payments platform for the global insurance industry, serving international health, life, and travel insurers, MGAs, brokers, and partners.

We need a professional, premium business card for use at insurance conferences and executive meetings. The goal is to create a card that feels trustworthy, modern, and high-quality, while still being distinctive and memorable in a stack of business cards.

Target audience:
Senior insurance executives (VP, C-suite).

Design goals:
Clear, professional, and credible
Modern but not trendy
Premium and well-structured
Easy to read and practical for networking

Brand direction:
Brand-first (company over individual)
Follow existing brand guidelines where possible
Clean layout, strong hierarchy, excellent readability

Must include:
Name
Title
Company name (Veltrix)
Logo
Email
Phone/Whatsapp
Website (www.withveltrix.example)
Tagline - Trust that moves money

Materials & finish:
Open to designer recommendations for premium look and feel.

Please avoid:
Flashy or trendy startup styles
Generic insurance icons or clichés
Cluttered layouts or hard-to-read text

Deliverables:
Front and back business card, print-ready files.

Target Market(s)

Global Insurance executives

Industry/Entity Type

Fintech, Insurtech, Insurance, Financial Services

Contact Information for Business Card

Name Title Company name (Veltrix) Logo Email Phone/Whatsapp Website (www.withveltrix.example) Tagline - Trust that moves money

Font styles to use
Other font styles liked:
• See brand guidelines

Requirements
Nice to have
• something that stands out/makes us more memorable while still remaining professional
Should not have
• Please avoid: Flashy or trendy startup styles Generic insurance icons or clichés Cluttered layouts or hard-to-read text

```html
<!DOCTYPE html>
<html lang="en">
<head>
<meta charset="utf-8">
<title>Veltrix — Business Card, Front and Back</title>
<link rel="stylesheet" href="https://fonts.googleapis.com/css2?family=Montserrat:wght@400;500;600&display=swap">
<style>
  :root {
    --page-bg: #e6e6e6;
    --card-bg: #ffffff;
    --ink: #111111;
    --ink-soft: #333333;
    --orange: #f7830f;
    --sunflower: #f3c366;
    --lavender: #d9c8f5;
    --peach: #fbdcc0;
    --sky: #c7e4f7;
    --aqua: #c2f0f4;
  }
  * { box-sizing: border-box; margin: 0; padding: 0; }
  html, body {
    width: 1200px; height: 849px; overflow: hidden;
    background: var(--page-bg);
    font-family: "Montserrat", sans-serif;
    color: var(--ink);
  }
  .sheet {
    position: relative; width: 1200px; height: 849px;
    display: flex; flex-direction: column; align-items: center; justify-content: center; gap: 46px;
  }
  .card {
    position: relative; width: 520px; height: 297px;
    background: var(--card-bg); overflow: hidden;
    box-shadow: 0 1px 3px rgba(0,0,0,0.08);
  }

  /* Back */
  .card-back__field {
    position: absolute; left: 0; top: 0; width: 100%; height: 272px;
    background: linear-gradient(120deg, rgba(251,220,192,0.28), rgba(217,200,245,0.22) 45%, rgba(199,228,247,0.3));
  }
  .card-back__brand {
    position: absolute; left: 0; top: 0; width: 100%; height: 272px;
    display: flex; flex-direction: column; align-items: center; justify-content: center; gap: 10px;
  }
  .card-back__lockup { display: flex; align-items: center; gap: 14px; }
  .brand-dot { width: 30px; height: 30px; border-radius: 50%; background: var(--orange); flex: none; }
  .card-back__name { font-size: 38px; font-weight: 500; letter-spacing: 0.08em; line-height: 1; }
  .card-back__tagline {
    font-size: 11px; font-weight: 500; letter-spacing: 0.28em; text-transform: uppercase;
    color: var(--ink-soft); padding-left: 44px;
  }
  .card-back__bands { position: absolute; left: 0; bottom: 0; width: 100%; height: 25px; }
  .band { position: absolute; top: 0; height: 100%; }
  .band--sunflower { left: 0; width: 48.8%; background: var(--sunflower); }
  .band--orange { right: 0; width: 48.8%; background: var(--orange); }

  /* Front */
  .card-front__wash {
    position: absolute; right: 0; top: 0; width: 48%; height: 100%;
    background: linear-gradient(160deg, rgba(217,200,245,0.75) 0%, rgba(251,220,192,0.55) 45%, rgba(199,228,247,0.7) 75%, rgba(194,240,244,0.7) 100%);
    clip-path: polygon(45% 0, 100% 0, 100% 100%, 0 100%);
  }
  .card-front__curves { position: absolute; inset: 0; width: 100%; height: 100%; }
  .card-front__brand {
    position: absolute; left: 70px; top: 88px;
    display: flex; flex-direction: column; gap: 6px;
  }
  .card-front__lockup { display: flex; align-items: center; gap: 10px; }
  .card-front__lockup .brand-dot { width: 22px; height: 22px; }
  .card-front__brand-name { font-size: 30px; font-weight: 500; letter-spacing: 0.02em; line-height: 1; }
  .card-front__tagline { font-size: 9px; font-weight: 500; letter-spacing: 0.14em; text-transform: uppercase; color: var(--ink-soft); padding-left: 32px; }
  .card-front__accent {
    position: absolute; right: 0; top: 40px; width: 15px; height: 37px; background: var(--orange);
  }
  .person { position: absolute; right: 50px; top: 38px; }
  .person__name {
    font-size: 27px; font-weight: 500; line-height: 1.1;
    border-bottom: 1.5px solid var(--ink); padding-bottom: 1px;
  }
  .person__title { font-size: 12px; letter-spacing: 0.45em; margin-top: 1px; }
  .contacts { position: absolute; right: 44px; top: 109px; list-style: none; }
  .contact {
    display: flex; align-items: center; justify-content: flex-end; gap: 16px;
    height: 26px; margin-bottom: 12px; font-size: 10.5px; white-space: nowrap;
  }
  .contact__icon {
    width: 26px; height: 26px; border-radius: 50%; background: var(--ink);
    display: flex; align-items: center; justify-content: center; flex: none;
  }
  .contact__icon svg { width: 14px; height: 14px; }
</style>
</head>
<body>
<main class="sheet">

  <section class="card card-back" aria-label="Card back">
    <div class="card-back__field" role="img" aria-label="Faint repeating brand pattern in peach, lavender and sky blue"></div>
    <div class="card-back__brand">
      <div class="card-back__lockup">
        <span class="brand-dot"></span>
        <span class="card-back__name">VELTRIX</span>
      </div>
      <p class="card-back__tagline">Trust that moves money</p>
    </div>
    <div class="card-back__bands">
      <span class="band band--sunflower"></span>
      <span class="band band--orange"></span>
    </div>
  </section>

  <section class="card card-front" aria-label="Card front">
    <div class="card-front__wash" role="img" aria-label="Large faint brand symbol decoration in lavender, peach and blue"></div>
    <svg class="card-front__curves" viewBox="0 0 520 297" preserveAspectRatio="none" aria-hidden="true">
      <path d="M0,176 Q150,255 328,297 L0,297 Z" fill="var(--sunflower)"/>
      <path d="M0,150 Q170,245 372,297" fill="none" stroke="var(--orange)" stroke-width="5"/>
    </svg>

    <div class="card-front__brand">
      <div class="card-front__lockup">
        <span class="brand-dot"></span>
        <span class="card-front__brand-name">Veltrix</span>
      </div>
      <p class="card-front__tagline">Trust that moves money</p>
    </div>

    <span class="card-front__accent"></span>

    <div class="person">
      <p class="person__name">Your Name</p>
      <p class="person__title">Title</p>
    </div>

    <ul class="contacts">
      <li class="contact"><span>Your number</span>
        <span class="contact__icon"><svg viewBox="0 0 24 24"><path fill="#fff" d="M6.6 10.8a15 15 0 0 0 6.6 6.6l2.2-2.2c.3-.3.7-.4 1-.2 1.1.4 2.3.6 3.6.6.6 0 1 .4 1 1V20c0 .6-.4 1-1 1A17 17 0 0 1 3 4c0-.6.4-1 1-1h3.5c.6 0 1 .4 1 1 0 1.3.2 2.5.6 3.6.1.3 0 .7-.2 1z"/></svg></span></li>
      <li class="contact"><span>Your email</span>
        <span class="contact__icon"><svg viewBox="0 0 24 24" fill="none" stroke="#fff" stroke-width="1.6"><rect x="3" y="6" width="18" height="12"/><path d="M3 6l9 7 9-7M3 18l7-6M21 18l-7-6"/></svg></span></li>
      <li class="contact"><span>www.withveltrix.example</span>
        <span class="contact__icon"><svg viewBox="0 0 24 24" fill="none" stroke="#fff" stroke-width="1.4"><circle cx="12" cy="12" r="9"/><ellipse cx="12" cy="12" rx="4" ry="9"/><path d="M3 12h18M5 7.5h14M5 16.5h14"/></svg></span></li>
      <li class="contact"><span>Your address</span>
        <span class="contact__icon"><svg viewBox="0 0 24 24"><path fill="#fff" d="M12 2a7 7 0 0 0-7 7c0 5 7 13 7 13s7-8 7-13a7 7 0 0 0-7-7zm0 9.5A2.5 2.5 0 1 1 12 6.5a2.5 2.5 0 0 1 0 5z"/></svg></span></li>
    </ul>
  </section>

</main>
</body>
</html>
```